Golf Course Hole Sign

I need signs designed for each hole of an 18-hole course.

Each sign will be have a similar design, but different information on each (such as the hole number, yardage, name of the hole, etc.).

Just to be clear, I just need ONE DESIGN. And, then the different course layouts & information can be pasted for each hole, once selected.

The theme of the course is the historical champions of golf, so a historical emphasis would be great. Each hole is named after a golfer.

Sign size: 24-inches wide X 15-inches high.

The sign must contain:
-Hole Number
-Hole Yardage
-Hole layout
-Name of Hole
-Picture of Golfer
-Description?
-Logo of course

I attached a sample to give you an idea of what a sign looks like (but it needs to have all the above information and in the dimension listed above). Also attached, the course layout for the first 6 holes, and the logo.

Target Market(s)

Golfers.

Industry/Entity Type

Golf Course

Requirements
Must have
• Hole layout
Hole Number
Hole Yardage
Name of Hole
Picture of Golfer
Description?
Logo of course

```html
<!DOCTYPE html>
<html lang="en">
<head>
<meta charset="UTF-8">
<title>Hole 12 Sign</title>
<link rel="stylesheet" href="https://fonts.googleapis.com/css2?family=Jost:wght@400;500;700;800&display=swap">
<style>
  :root {
    --bg: #3b2719;
    --frame: #8e7d6d;
    --layout-fill: #776757;
    --wreath: #5a4535;
    --text: #ffffff;
    --photo-light: #cbbfae;
    --photo-dark: #6b5c4b;
  }
  html, body {
    margin: 0;
    padding: 0;
    width: 1200px;
    height: 750px;
    overflow: hidden;
    background: var(--bg);
  }
  .sign {
    position: relative;
    width: 1200px;
    height: 750px;
    background: var(--bg);
    font-family: "Jost", sans-serif;
    color: var(--text);
  }
  .frame {
    position: absolute;
    inset: 0;
  }
  .hole-badge {
    position: absolute;
    left: 148px;
    top: 105px;
    width: 240px;
    height: 240px;
    border-radius: 50%;
    background: var(--wreath);
  }
  .hole-label {
    position: absolute;
    left: 168px;
    width: 200px;
    top: 160px;
    text-align: center;
    font-size: 33px;
    font-weight: 500;
    line-height: 1;
    letter-spacing: 0.5px;
  }
  .hole-number {
    position: absolute;
    left: 168px;
    width: 200px;
    top: 190px;
    text-align: center;
    font-size: 80px;
    font-weight: 700;
    line-height: 1;
  }
  .stats {
    position: absolute;
    left: 138px;
    width: 258px;
    top: 362px;
    text-align: center;
  }
  .par {
    font-size: 46px;
    font-weight: 700;
    line-height: 1;
    margin: 0;
    padding-bottom: 17px;
    border-bottom: 2px dotted var(--frame);
  }
  .yardage-title {
    font-size: 28px;
    font-weight: 700;
    margin: 18px 0 12px;
    line-height: 1;
    letter-spacing: 0.5px;
  }
  .yardage-list {
    list-style: none;
    margin: 0;
    padding: 0;
    font-size: 30px;
    font-weight: 400;
    line-height: 33px;
  }
  .course-logo {
    margin-top: 32px;
    font-size: 18px;
    font-weight: 700;
    letter-spacing: 0.5px;
  }
  .hole-layout {
    position: absolute;
    left: 462px;
    top: 158px;
    width: 256px;
    height: 444px;
    border-radius: 120px;
    background: var(--layout-fill);
  }
  .golfer-photo {
    position: absolute;
    left: 782px;
    top: 72px;
    width: 284px;
    height: 284px;
    border-radius: 50%;
    background: radial-gradient(circle at 50% 40%, var(--photo-light), var(--photo-dark));
  }
  .golfer {
    position: absolute;
    left: 803px;
    top: 382px;
    width: 290px;
  }
  .golfer-name {
    font-size: 40px;
    font-weight: 700;
    margin: 0 0 14px;
    line-height: 1.1;
    letter-spacing: 0.3px;
  }
  .golfer-bio {
    font-size: 18px;
    line-height: 22.8px;
    margin: 0;
  }
</style>
</head>
<body>
<main class="sign">
  <svg class="frame" width="1200" height="750" viewBox="0 0 1200 750" aria-hidden="true">
    <polygon points="60,17 1140,17 1183,60 1183,690 1140,733 60,733 17,690 17,60"
             fill="none" stroke="var(--frame)" stroke-width="5"/>
    <circle cx="44" cy="44" r="16" fill="var(--frame)"/>
    <circle cx="1156" cy="44" r="16" fill="var(--frame)"/>
    <circle cx="44" cy="706" r="16" fill="var(--frame)"/>
    <circle cx="1156" cy="706" r="16" fill="var(--frame)"/>
    <rect x="72" y="40" width="66" height="66" rx="20" fill="var(--frame)" role="img" aria-label="Corner flourish ornament"/>
    <rect x="1062" y="40" width="66" height="66" rx="20" fill="var(--frame)" role="img" aria-label="Corner flourish ornament"/>
    <rect x="72" y="644" width="66" height="66" rx="20" fill="var(--frame)" role="img" aria-label="Corner flourish ornament"/>
    <rect x="1062" y="644" width="66" height="66" rx="20" fill="var(--frame)" role="img" aria-label="Corner flourish ornament"/>
  </svg>

  <section class="hole-info">
    <div class="hole-badge" role="img" aria-label="Laurel wreath ornament around the hole number"></div>
    <div class="hole-label">HOLE</div>
    <div class="hole-number">12</div>

    <div class="stats">
      <p class="par">PAR 5</p>
      <p class="yardage-title">YARDAGE</p>
      <ul class="yardage-list">
        <li>White: 180</li>
        <li>Red: 253</li>
        <li>Blue: 305</li>
      </ul>
      <div class="course-logo">LOGO</div>
    </div>
  </section>

  <div class="hole-layout" role="img" aria-label="Hole layout map showing fairway shape and green"></div>

  <section class="golfer-panel">
    <div class="golfer-photo" role="img" aria-label="Sepia portrait photograph of the golfer the hole is named after"></div>
    <div class="golfer">
      <h1 class="golfer-name">Harlan Pike</h1>
      <p class="golfer-bio">Name Name volorrum hicia sollab id eos doluptam lam eaturOffici consendis doluptur. Venducipit, omnient volorum et vit as nihillu ptatio. Imolum con nis sequi blaut vello te molupiendi quae dolupta cum litatiusae nimagnatium quaspelis poraepe rovitas inullor.</p>
    </div>
  </section>
</main>
</body>
</html>
```